VelmoraTrade (Trading Platform)

We need a design of VelmoraTrade Trading Platform.

Please find attached a mock up of VelmoraTrade design this has to be redesigned based on plinor.co.uk style.

Industry/Entity Type

Digital

```html
<!DOCTYPE html>
<html lang="en">
<head>
<meta charset="utf-8">
<title>VelmoraTrade – Trading</title>
<link rel="stylesheet" href="https://fonts.googleapis.com/css2?family=Roboto:wght@400;500;700&family=Roboto+Condensed:wght@400;700&display=swap">
<style>
:root{
  --blue:#0099d6;
  --blue-light:#3bb3e3;
  --ink:#222;
  --text:#333;
  --muted:#777;
  --line:#d6d6d6;
  --band:#e8e8e8;
  --field:#f1f1f1;
  --dark:#2b2b2b;
  --area:#daf2fb;
  --stroke:#9fd9f0;
  --down:#d0021b;
  --up:#2aa12a;
}
*{box-sizing:border-box;margin:0;padding:0}
html,body{width:1200px;height:838px;overflow:hidden;background:#fff}
body{position:relative;font-family:"Roboto",Arial,sans-serif;font-size:11.5px;color:var(--text)}
.abs{position:absolute}
/* header */
.site-header{left:0;top:0;width:1200px;height:83px}
.brand{left:162px;top:24px;font-size:17px;font-weight:500;color:var(--ink);letter-spacing:.4px;display:flex;align-items:center;gap:8px;white-space:nowrap}
.brand-dot{width:13px;height:13px;border-radius:50%;background:var(--blue)}
.brand-rule{left:303px;top:12px;width:1px;height:57px;background:var(--line)}
.main-nav{left:317px;top:59px;font-size:11px;color:#555;white-space:nowrap}
.login{left:678px;top:35px;display:flex;gap:6px;align-items:center}
.field{height:23px;border:1px solid #ccc;font-size:11px;color:#888;padding:5px 8px;background:#fff}
.field.email{width:116px}
.field.pass{width:116px}
.btn{height:21px;border-radius:2px;color:#fff;font-size:10px;display:flex;align-items:center;justify-content:center}
.btn.login-btn{width:48px;background:#555}
.btn.signup-btn{width:48px;background:var(--blue)}
.forgot{left:679px;top:61px;font-size:8.5px;color:#888}
/* ticker band */
.ticker{left:0;top:83px;width:1200px;height:43px;background:var(--blue);color:#fff}
.coin{left:273px;top:7px;width:29px;height:29px;border-radius:50%;border:2px solid #fff}
.stat{top:5px;height:33px;padding-left:14px;border-left:1px solid rgba(255,255,255,.35);white-space:nowrap}
.stat .label{font-size:9.5px;opacity:.95}
.stat .value{font-size:13px;margin-top:2px}
.stat .value small{font-size:9px}
.stat.first{border-left:none;padding-left:0}
/* title band */
.page-title{left:0;top:126px;width:1200px;height:68px;background:var(--band);border-bottom:1px solid #c8c8c8}
.page-title h1{position:absolute;left:175px;top:15px;font-family:"Roboto Condensed",Arial,sans-serif;font-weight:700;font-size:30px;color:#111}
/* panels */
.panel{border:1px solid var(--line);background:#fff;overflow:hidden}
table{border-collapse:collapse;width:100%}
td,th{text-align:left;font-weight:400;white-space:nowrap}
.grid th{font-family:"Roboto Condensed",Arial,sans-serif;font-weight:700;font-size:12px;color:#222;height:26px;padding-left:9px;border-bottom:1px solid var(--line)}
.grid td{height:22.5px;padding-left:9px;border-bottom:1px solid #e4e4e4;font-size:11px}
.grid th+th,.grid td+td{border-left:1px solid var(--line)}
.grid tr:last-child td{border-bottom:none}
.arrow{font-size:9px;margin-right:3px}
.arrow.down{color:var(--down)}
.arrow.up{color:var(--up)}
/* chat */
.tabs{display:flex;height:26px;border-bottom:1px solid var(--line);background:#fff}
.tab{padding:0 8px;display:flex;align-items:center;font-size:11px;border-right:1px solid var(--line);white-space:nowrap}
.tab.active{background:var(--dark);color:#fff}
.chat-tabs .tab{padding:0 6px;font-size:10.5px}
.chat-tabs .tab:last-child{flex:1;justify-content:center;padding:0 4px}
.chat-log{padding:10px 9px;font-size:11px;line-height:18px}
.chat-input{position:absolute;left:6px;bottom:6px;width:117px;height:22px;border:1px solid #ccc;font-size:10.5px;color:#444;padding:4px 6px;white-space:nowrap;overflow:hidden}
/* chart */
.toolbar{height:44px;background:var(--band);border-bottom:1px solid var(--line);display:flex;align-items:center;padding-left:13px;gap:0}
.tb{height:22px;background:var(--blue);color:#fff;font-size:12.5px;font-weight:500;display:flex;align-items:center;position:relative}
.tb .caret{width:17px;height:22px;border-left:1px solid rgba(255,255,255,.6);display:flex;align-items:center;justify-content:center}
.subbar{height:41px;background:#fafafa;border-bottom:1px solid var(--line);position:relative}
.select-tool{position:absolute;left:12px;top:7px;width:103px;height:24px;border:1px solid #ccc;background:#fff;font-size:12px;padding:4px 15px;color:#222;white-space:nowrap}
.select-tool .c{position:absolute;right:0;top:0;width:17px;height:22px;border-left:1px solid #ccc;font-size:8px;color:#999;text-align:center;line-height:22px}
.ohlc{position:absolute;top:6px;font-size:10.5px;line-height:13px;color:#333;white-space:nowrap}
.axis{position:absolute;top:327px;font-size:10.5px;color:#888;white-space:nowrap}
/* orders */
.orders .grid th{font-family:"Roboto",Arial,sans-serif;font-weight:500;background:var(--band);height:24px;font-size:11px}
.orders .grid td{height:24px}
.orders .grid tr:last-child td{height:22px}
/* market */
.mk-tabs{display:flex;height:29px}
.mk-tabs div{flex:1;display:flex;align-items:center;justify-content:center;font-family:"Roboto Condensed",Arial,sans-serif;font-weight:700;font-size:12.5px}
.mk-tabs .active{background:var(--dark);color:#fff}
.mk-tabs .off{background:var(--band);color:#222}
.mk-body{display:flex;border-top:1px solid var(--line)}
.mk-col{flex:1;text-align:center}
.mk-col+.mk-col{border-left:1px solid var(--line)}
.mk-col .kind{color:var(--blue);font-size:13px;margin-top:10px}
.mk-col .quote{font-size:12px;color:#555}
.mk-col .quote b{font-size:16px;color:#222;font-weight:500}
.mk-col .qty{border-top:1px solid var(--line);margin-top:8px;height:28px;line-height:28px;color:#aaa;font-size:12px}
.flabel{top:351px;font-size:12.5px;color:#222}
.fbox{top:371px;height:19px;background:var(--field);border:1px solid #e2e2e2;font-size:12.5px;padding:1px 6px;color:#333}
/* footer */
.site-footer{left:0;top:773px;width:1200px;height:65px;background:var(--blue);color:#fff;text-align:center;font-size:12px;padding-top:17px;line-height:18px}
.site-footer .links{color:#fff}
</style>
</head>
<body>

<header class="site-header abs">
  <div class="brand abs"><span>VelmoraTrade</span><span class="brand-dot"></span></div>
  <div class="brand-rule abs"></div>
  <nav class="main-nav abs">Home · About · Trading · Support</nav>
  <form class="login abs">
    <div class="field email">Email</div>
    <div class="field pass">Password</div>
    <div class="btn login-btn">Log In</div>
    <div class="btn signup-btn">Sign Up</div>
  </form>
  <div class="forgot abs">Forgot your password?</div>
</header>

<section class="ticker abs">
  <div class="coin abs"></div>
  <div class="stat first abs" style="left:312px"><div class="label">Current Price</div><div class="value">$444.13</div></div>
  <div class="stat abs" style="left:398px"><div class="label">Daily Change</div><div class="value">-9.54 <small>-2.10%</small></div></div>
  <div class="stat abs" style="left:499px"><div class="label">Day's Range</div><div class="value">$440.00 - $457.30</div></div>
  <div class="stat abs" style="left:646px"><div class="label">Today's Open</div><div class="value">$453.57</div></div>
  <div class="stat abs" style="left:749px"><div class="label">24h Volume</div><div class="value">7194 BTC</div></div>
</section>

<section class="page-title abs"><h1>Trading</h1></section>

<!-- left column -->
<div class="panel abs" style="left:176px;top:226px;width:129px;height:128px">
  <table class="grid">
    <tr><th style="width:66px">PAIR</th><th>PRICE</th></tr>
    <tr><td>BTC/USD</td><td><span class="arrow down">⬇</span>634.12</td></tr>
    <tr><td>LTC/USD</td><td><span class="arrow down">⬇</span>23.23</td></tr>
    <tr><td>LTC/BTC</td><td><span class="arrow up">⬆</span>0.0123</td></tr>
    <tr><td style="height:27px"></td><td></td></tr>
  </table>
</div>

<div class="panel abs" style="left:176px;top:375px;width:129px;height:129px">
  <table class="grid">
    <tr><th colspan="2">YOUR BALANCE</th></tr>
    <tr><td style="width:58px">BTC</td><td>0.92176</td></tr>
    <tr><td>LTC</td><td>0</td></tr>
    <tr><td>USD</td><td>1987.45</td></tr>
    <tr><td style="height:27px"></td><td></td></tr>
  </table>
</div>

<div class="panel abs" style="left:176px;top:525px;width:129px;height:212px">
  <div class="tabs chat-tabs">
    <div class="tab active">Chat</div>
    <div class="tab">News</div>
    <div class="tab" style="border-right:none">Chirper</div>
  </div>
  <div class="chat-log">User1 : &nbsp;Hello!<br>User2 : &nbsp;Hiii</div>
  <div class="chat-input">Type your message ...</div>
</div>

<!-- chart -->
<div class="panel abs" style="left:326px;top:227px;width:474px;height:359px">
  <div class="toolbar">
    <div class="tb" style="width:147px;background:var(--blue-light)"><span style="margin-left:auto;padding-right:7px;background:var(--blue);height:22px;line-height:22px;padding-left:6px">1D</span><span class="caret" style="background:var(--blue)">▾</span></div>
    <div class="tb" style="margin-left:16px;width:81px"><span style="flex:1;text-align:center">Chart</span><span class="caret">▾</span></div>
    <div class="tb" style="margin-left:19px;width:81px"><span style="flex:1;text-align:center">Studies</span><span class="caret">▾</span></div>
    <div class="tb" style="margin-left:19px;width:47px"><span style="flex:1;text-align:center">⚙</span><span class="caret">▾</span></div>
    <div class="tb" style="margin-left:17px;width:24px;justify-content:center">F</div>
  </div>
  <div class="subbar">
    <div class="select-tool">Select Tool<span class="c">▾</span></div>
    <div class="ohlc" style="left:285px">O: &nbsp;140.13<br>C: &nbsp;141.35</div>
    <div class="ohlc" style="left:352px">H: &nbsp;141.40<br>L: &nbsp;140.04</div>
    <div class="ohlc" style="left:418px">V: &nbsp;65.4m</div>
  </div>
  <svg class="abs" style="left:0;top:85px" width="474" height="226" viewBox="0 0 474 226" aria-label="Price chart">
    <g stroke="#e3e3e3" stroke-width="1">
      <line x1="0" y1="41" x2="474" y2="41"/><line x1="0" y1="88" x2="474" y2="88"/>
      <line x1="0" y1="134" x2="474" y2="134"/><line x1="0" y1="180" x2="474" y2="180"/>
    </g>
    <path d="M0 123 L21 130 L54 117 L61 120 L131 77 L140 85 L153 78 L201 125 L236 125 L258 148 L271 134 L308 148 L346 100 L372 100 L390 132 L403 112 L428 155 L443 136 L463 152 L474 136 L474 226 L0 226 Z" fill="var(--area)" stroke="none"/>
    <path d="M0 123 L21 130 L54 117 L61 120 L131 77 L140 85 L153 78 L201 125 L236 125 L258 148 L271 134 L308 148 L346 100 L372 100 L390 132 L403 112 L428 155 L443 136 L463 152 L474 136" fill="none" stroke="var(--stroke)" stroke-width="1.2"/>
    <line x1="0" y1="225.5" x2="474" y2="225.5" stroke="#d0d0d0"/>
  </svg>
  <span class="axis" style="left:43px">05 Apr</span>
  <span class="axis" style="left:114px">10 Apr</span>
  <span class="axis" style="left:185px">15 Apr</span>
  <span class="axis" style="left:256px">20 Apr</span>
  <span class="axis" style="left:327px">25 Apr</span>
  <span class="axis" style="left:398px">30 Apr</span>
</div>

<!-- orders -->
<div class="panel orders abs" style="left:326px;top:614px;width:474px;height:123px">
  <div class="tabs">
    <div class="tab active" style="padding:0 9px">Orders</div>
    <div class="tab" style="padding:0 10px">History</div>
    <div class="tab" style="border-right:none;padding:0 12px">Transaction</div>
  </div>
  <table class="grid">
    <tr><th style="width:127px">Tickers</th><th style="width:186px">Time</th><th style="width:82px">Price</th><th>Volume</th></tr>
    <tr><td>BTC/USD</td><td>12:23 12.10.2014</td><td>634.34</td><td>0.23</td></tr>
    <tr><td>LTC/USD</td><td>11:23 12.10.2014</td><td>23.45</td><td>0.01</td></tr>
    <tr><td></td><td></td><td></td><td></td></tr>
  </table>
</div>

<!-- market -->
<div class="panel abs" style="left:822px;top:226px;width:200px;height:110px">
  <div class="mk-tabs"><div class="active">MARKET</div><div class="off">LIMIT</div></div>
  <div class="mk-body">
    <div class="mk-col"><div class="kind">LIMIT SELL</div><div class="quote">157 <b>5.6</b> 0</div><div class="qty">Qty &nbsp;20.0</div></div>
    <div class="mk-col"><div class="kind">LIMIT BUY</div><div class="quote">157 <b>5.7</b> 1</div><div class="qty">Qty &nbsp;20.0</div></div>
  </div>
</div>

<div class="flabel abs" style="left:821px">Quantity</div>
<div class="flabel abs" style="left:903px">Limit</div>
<div class="fbox abs" style="left:822px;width:69px">50</div>
<div class="fbox abs" style="left:903px;width:118px">1576.63</div>

<div class="panel abs" style="left:822px;top:410px;width:200px;height:327px">
  <table class="grid">
    <tr><th style="width:100px">PRICE</th><th>VOLUME</th></tr>
    <tr><td>123</td><td>0.223</td></tr>
    <tr><td>122</td><td>0.331</td></tr>
    <tr><td>119</td><td>2.321</td></tr>
    <tr><td>118</td><td>0.343</td></tr>
    <tr><td>117</td><td>0.22</td></tr>
    <tr><td>116</td><td>0.025</td></tr>
    <tr><td>115</td><td>0.5246</td></tr>
    <tr><td>114</td><td>0.546</td></tr>
    <tr><td>113</td><td>1.275</td></tr>
    <tr><td>112</td><td>2.343</td></tr>
    <tr><td>111</td><td>0.232</td></tr>
    <tr><td>110</td><td>0.244</td></tr>
    <tr><td>109</td><td>0.821</td></tr>
  </table>
</div>

<footer class="site-footer abs">
  Copyright © 2014 VelmoraTrade. All rights reserved.<br>
  <span class="links">Terms &amp; Condition &nbsp;&nbsp;| &nbsp;&nbsp;FAQ</span>
</footer>

</body>
</html>
```